Meridian Rest Supply Needs Business Card

Looking for a very nice looking business card. Creative but not extravagant. We sell beds and pillows across the U.S. and need something professional but catchy. I have attached the logo.

Name : Dale Fenwick
Title : President
Phone : (800) 417-2964
Email: sleep@quorvana.com
Website: www.quorvana.com

Can be single-sided or double-sided
horizontal or vertical

Can use Blues/Greys

Target Market(s)

Mass Market

Industry/Entity Type

Retail

Contact Information for Business Card

Name : Dale Fenwick
Title : President
Phone : (800) 417-2964
Email: sleep@quorvana.com
Website: www.quorvana.com

Requirements
Must have
• Clean, Modern, Smooth
• Can use Blues/Greys
• On the other side without the information - have something simple like www.quorvana.com or our logo
Nice to have
• Surprise me
Should not have
• Nothing crazy, nothing cluttered

```html
<!DOCTYPE html>
<html lang="en">
<head>
<meta charset="utf-8">
<title>Quorvana Business Card</title>
<link rel="stylesheet" href="https://fonts.googleapis.com/css2?family=Arimo:wght@400;700&display=swap">
<style>
  :root {
    --backdrop: #3a3330;
    --card-white: #ffffff;
    --brand-blue: #35a5d8;
    --text-white: #ffffff;
    --rule-light: rgba(255, 255, 255, 0.75);
  }
  * { margin: 0; padding: 0; box-sizing: border-box; }
  html, body {
    width: 1200px;
    height: 769px;
    overflow: hidden;
    background: var(--backdrop);
    font-family: "Arimo", Arial, sans-serif;
  }
  .canvas {
    position: relative;
    width: 1200px;
    height: 769px;
  }
  .card {
    position: absolute;
    top: 236px;
    width: 520px;
    height: 297px;
    box-shadow: 0 10px 24px rgba(0, 0, 0, 0.45);
  }
  .card--front {
    left: 50px;
    background: var(--card-white);
    display: flex;
    align-items: center;
    justify-content: center;
  }
  .card--back {
    left: 630px;
    background: var(--brand-blue);
    color: var(--text-white);
  }
  .wordmark {
    font-weight: 400;
    letter-spacing: 2px;
    line-height: 1;
  }
  .card--front .wordmark {
    color: var(--brand-blue);
    font-size: 68px;
  }
  .card--back .wordmark {
    position: absolute;
    right: 42px;
    top: 62px;
    color: var(--text-white);
    font-size: 50px;
  }
  .rule {
    position: absolute;
    left: 38px;
    right: 38px;
    height: 1px;
    background: var(--rule-light);
  }
  .rule--top { top: 172px; }
  .rule--bottom { top: 262px; }
  .contact-name {
    position: absolute;
    top: 190px;
    left: 0;
    right: 0;
    text-align: center;
    font-size: 16px;
  }
  .contact-name strong { font-weight: 700; }
  .contact-details {
    position: absolute;
    top: 222px;
    left: 0;
    right: 0;
    text-align: center;
    font-size: 12px;
    white-space: nowrap;
  }
  .contact-details b { font-weight: 700; }
  .contact-details span + span { margin-left: 10px; }
</style>
</head>
<body>
<main class="canvas">
  <section class="card card--front" aria-label="Card front">
    <div class="wordmark">quorvana</div>
  </section>

  <section class="card card--back" aria-label="Card back">
    <div class="wordmark">quorvana</div>
    <div class="rule rule--top"></div>
    <p class="contact-name"><strong>Dale Fenwick -</strong> President</p>
    <p class="contact-details">
      <span><b>P:</b> (800) 417-2964</span>
      <span><b>E:</b> sleep@quorvana.com</span>
      <span><b>W:</b> www.quorvana.com</span>
    </p>
    <div class="rule rule--bottom"></div>
  </section>
</main>
</body>
</html>
```